Letterhead business card with cool logo

Name of Business: Marcus T Holloway Certified General Accountant

Trade Name: Holloway, DRQ

I am looking to create a front page for letter, subsequent page and business card that all tie in together with the same theme.
I am a one person accounting office that prepares personal and corporate tax returns and financial statements, i also provide estate and financial planning, payroll services, bookkepping...

i am kinda thinking some thing like thought bubble, gears in the slhouette of a head, someting contempary indicating intellectual property.

letterhead and business card must incorporate space for return address, email address and phone number

please also include either the blue or black DRQ logo

Industry/Entity Type

Accounting

Requirements
Must have
• incorporate space for return address, email address and phone number

```html
<!DOCTYPE html>
<html lang="en">
<head>
<meta charset="UTF-8">
<title>Marcus T Holloway — Letterhead</title>
<link rel="stylesheet" href="https://fonts.googleapis.com/css2?family=Marcellus+SC&family=Montserrat:wght@400;500&family=Lato:wght@400&display=swap">
<style>
  :root {
    --canvas-bg: #ffffff;
    --paper: #ffffff;
    --brand-blue: #1f4f9a;
    --brand-blue-light: #2f7fd0;
    --ink: #333333;
    --watermark: #f0f0f0;
  }
  html, body {
    margin: 0;
    padding: 0;
    width: 1200px;
    height: 1000px;
    overflow: hidden;
    background: var(--canvas-bg);
  }
  .letterhead {
    position: absolute;
    left: 250px;
    top: 48px;
    width: 700px;
    height: 905px;
    background: var(--paper);
    overflow: hidden;
    outline: 1px solid #ececec;
  }
  .watermark {
    position: absolute;
    left: 0;
    top: 350px;
    width: 490px;
    height: 510px;
  }
  .brand-mark {
    position: absolute;
    left: 50%;
    top: 12px;
    transform: translateX(-50%);
  }
  .brand-name {
    position: absolute;
    top: 108px;
    left: 0;
    width: 100%;
    margin: 0;
    text-align: center;
    font-family: "Marcellus SC", serif;
    font-weight: 400;
    font-size: 34px;
    letter-spacing: 1px;
    color: var(--brand-blue);
  }
  .brand-title {
    position: absolute;
    top: 154px;
    left: 0;
    width: 100%;
    margin: 0;
    text-align: center;
    font-family: "Montserrat", sans-serif;
    font-size: 12.5px;
    letter-spacing: 2px;
    text-transform: uppercase;
    color: var(--brand-blue);
  }
  .brand-title .designation {
    font-weight: 500;
    margin-right: 6px;
  }
  .contact-line {
    position: absolute;
    top: 806px;
    left: 0;
    width: 100%;
    margin: 0;
    text-align: center;
    font-family: "Lato", sans-serif;
    font-size: 13px;
    color: var(--ink);
    word-spacing: 2px;
  }
  .footer-band {
    position: absolute;
    left: 0;
    bottom: 0;
    width: 100%;
    height: 33px;
    background: var(--brand-blue);
  }
</style>
</head>
<body>
  <main class="letterhead">
    <svg class="watermark" viewBox="0 0 490 510" aria-hidden="true">
      <circle cx="230" cy="253" r="253" fill="var(--watermark)"/>
    </svg>

    <svg class="brand-mark" width="86" height="86" viewBox="0 0 86 86" aria-hidden="true">
      <circle cx="43" cy="43" r="42" fill="var(--brand-blue)"/>
    </svg>

    <h1 class="brand-name">Marcus T Holloway</h1>
    <p class="brand-title"><span class="designation">DRQ</span>Certified General Accountant</p>

    <p class="contact-line">Address * E-mail &nbsp;* &nbsp;Phone Number &nbsp;* &nbsp;Website</p>
    <div class="footer-band"></div>
  </main>
</body>
</html>
```